IT services company needs a business card designed

-2 sided business card.-Front is going to be the logo raised (3D floating effect) on a black background. Make the logos spider web shiny silver and keep the spider the same design. -Back needs to have the following information:Darrel Sotho, Managing Partner, Cell: 738-402-1954, Website: Plankhorn.com, Email: Darrel@Plankhorn.com
Target Market(s)
IT Services
Industry/Entity Type
It Company
Contact Information for Business Card
-2 sided business card.
-Front is going to be the logo raised (3D floating effect) on a black background. Make the logos spider web shiny silver and keep the spider the same design.
-Back needs to have the following information:
Darrel Sotho, Managing Partner, Cell: 738-402-1954, Website: Plankhorn.com, Email: Darrel@Plankhorn.com

```html
<!DOCTYPE html>
<html lang="en">
<head>
<meta charset="utf-8">
<title>Plankhorn Business Card</title>
<link href="https://fonts.googleapis.com/css2?family=Barlow:wght@400;500&display=swap" rel="stylesheet">
<style>
  :root {
    --page-bg: #ffffff;
    --front-top: #45484c;
    --front-mid: #1a1d21;
    --front-bottom: #03060a;
    --symbol-glow: rgba(190, 194, 200, 0.30);
    --symbol-glow-soft: rgba(120, 124, 130, 0.10);
    --symbol-tint: rgba(18, 168, 230, 0.22);
    --symbol-tint-soft: rgba(140, 140, 140, 0.10);
    --back-bg: #ffffff;
    --back-border: #5a5a5a;
    --text-grey: #555555;
    --wordmark-dark: #231f20;
    --wordmark-light: #ffffff;
    --dot-navy: #2f5873;
    --dot-mid: #1f86bf;
    --dot-sky: #12a8e6;
  }
  html, body {
    margin: 0;
    padding: 0;
    width: 1200px;
    height: 1000px;
    overflow: hidden;
    background: var(--page-bg);
    font-family: "Barlow", Arial, sans-serif;
  }
  .canvas {
    position: relative;
    width: 1200px;
    height: 1000px;
  }
  .card {
    position: absolute;
    left: 260px;
    width: 680px;
    height: 388px;
    box-sizing: border-box;
  }

  /* Front */
  .card-front {
    top: 60px;
    background: linear-gradient(to bottom, var(--front-top) 0%, var(--front-mid) 50%, var(--front-bottom) 100%);
  }
  .front-symbol {
    position: absolute;
    left: 232px;
    top: 32px;
    width: 214px;
    height: 242px;
    border-radius: 50%;
    background: radial-gradient(ellipse at center, var(--symbol-glow) 0%, var(--symbol-glow-soft) 55%, rgba(0,0,0,0) 75%);
  }
  .front-wordmark {
    position: absolute;
    left: 0;
    right: 0;
    top: 284px;
    margin: 0;
    text-align: center;
    color: var(--wordmark-light);
    font-size: 58px;
    font-weight: 400;
    letter-spacing: 1px;
    line-height: 1;
  }

  /* Back */
  .card-back {
    top: 540px;
    background: var(--back-bg);
    border: 1px solid var(--back-border);
  }
  .holder-name {
    position: absolute;
    left: 59px;
    top: 62px;
    margin: 0;
    color: var(--text-grey);
    font-size: 34px;
    font-weight: 400;
    line-height: 1.2;
  }
  .holder-title {
    position: absolute;
    left: 59px;
    top: 105px;
    margin: 0;
    color: var(--text-grey);
    font-size: 23px;
    font-weight: 400;
    line-height: 1.2;
  }
  .contact-list {
    position: absolute;
    left: 54px;
    top: 244px;
    margin: 0;
    padding: 0;
    list-style: none;
  }
  .contact-list li {
    display: flex;
    align-items: center;
    height: 32px;
    color: var(--text-grey);
    font-size: 23px;
  }
  .contact-list .bullet {
    width: 15px;
    height: 15px;
    border-radius: 50%;
    margin-right: 15px;
    flex: none;
  }
  .bullet-navy { background: var(--dot-navy); }
  .bullet-mid { background: var(--dot-mid); }
  .bullet-sky { background: var(--dot-sky); }
  .back-symbol {
    position: absolute;
    left: 392px;
    top: 48px;
    width: 192px;
    height: 210px;
    border-radius: 50%;
    background: radial-gradient(ellipse at center, var(--symbol-tint) 0%, var(--symbol-tint-soft) 55%, rgba(255,255,255,0) 75%);
  }
  .back-wordmark {
    position: absolute;
    left: 340px;
    width: 300px;
    top: 266px;
    margin: 0;
    text-align: center;
    color: var(--wordmark-dark);
    font-size: 54px;
    font-weight: 400;
    line-height: 1;
  }
</style>
</head>
<body>
<div class="canvas">
  <section class="card card-front" aria-label="Card front">
    <div class="front-symbol" role="img" aria-label="Raised silver brand symbol"></div>
    <p class="front-wordmark">PLANKHORN</p>
  </section>

  <section class="card card-back" aria-label="Card back">
    <h1 class="holder-name">Darrel Sotho</h1>
    <p class="holder-title">Managing Partner</p>
    <ul class="contact-list">
      <li><span class="bullet bullet-navy"></span>Cell: 738-402-1954</li>
      <li><span class="bullet bullet-mid"></span>Plankhorn.com</li>
      <li><span class="bullet bullet-sky"></span>Darrel@Plankhorn.com</li>
    </ul>
    <div class="back-symbol" role="img" aria-label="Blue and grey brand symbol"></div>
    <p class="back-wordmark">PLANKHORN</p>
  </section>
</div>
</body>
</html>
```